Global (re)insurance broker needs a business card design

We need a classic business card for our company that is headquartered in SG, with offices in Malaysia and Dubai. We specialise in insurance and reinsurance broking and consultancy for our global clients.

```html
<!DOCTYPE html>
<html lang="en">
<head>
<meta charset="utf-8">
<title>Norvane Business Card</title>
<link href="https://fonts.googleapis.com/css2?family=Poppins:wght@400;500;600;700&display=swap" rel="stylesheet">
<style>
  :root {
    --bg: #c4c4c4;
    --brand-blue: #27489a;
    --brand-green: #a9cfb0;
    --ink: #222428;
    --ghost-grey: #e4e4e4;
    --white: #ffffff;
  }
  * { box-sizing: border-box; margin: 0; padding: 0; }
  html, body { width: 1200px; height: 900px; overflow: hidden; }
  body {
    background: var(--bg);
    font-family: "Poppins", sans-serif;
    position: relative;
  }
  .card {
    position: absolute;
    width: 600px;
    height: 343px;
    border-radius: 26px;
    overflow: hidden;
    box-shadow: 0 10px 24px rgba(0,0,0,0.25);
  }
  /* Front */
  .card-front {
    left: 70px; top: 70px;
    background: linear-gradient(to bottom, var(--brand-green) 0%, #6f8fb0 35%, var(--brand-blue) 70%, var(--brand-blue) 100%);
  }
  .card-front .ghost-name {
    position: absolute;
    right: -70px; top: 120px;
    font-size: 150px; font-weight: 600;
    color: rgba(255,255,255,0.1);
    letter-spacing: 2px;
    line-height: 1;
    white-space: nowrap;
  }
  .card-front .wordmark {
    position: absolute;
    left: 0; right: 0; top: 118px;
    text-align: center;
    font-size: 72px; font-weight: 600;
    color: var(--white);
    letter-spacing: 3px;
    line-height: 1;
  }
  .card-front .tagline {
    position: absolute;
    left: 0; right: 0; top: 210px;
    text-align: center;
    font-size: 13px; font-weight: 400;
    color: var(--white);
    line-height: 1.35;
  }
  /* Back */
  .card-back {
    left: 530px; top: 487px;
    background: var(--white);
  }
  .card-back .ghost-name {
    position: absolute;
    left: 250px; top: 30px;
    font-size: 150px; font-weight: 600;
    color: var(--ghost-grey);
    letter-spacing: 2px;
    line-height: 1;
    white-space: nowrap;
  }
  .card-back .wordmark {
    position: absolute;
    left: 40px; top: 46px;
    font-size: 56px; font-weight: 600;
    color: var(--brand-blue);
    letter-spacing: 2px;
    line-height: 1;
  }
  .card-back .person {
    position: absolute;
    left: 40px; top: 152px;
  }
  .person-name {
    font-size: 21px; font-weight: 700;
    color: var(--brand-blue);
    letter-spacing: 0.5px;
    text-transform: uppercase;
    line-height: 1.15;
  }
  .person-role {
    font-size: 16px; font-weight: 400;
    color: var(--ink);
    line-height: 1.2;
  }
  .contact-list {
    list-style: none;
    margin-top: 14px;
  }
  .contact-list li {
    display: flex; align-items: center; gap: 8px;
    font-size: 15px; color: var(--ink);
    line-height: 1.5;
  }
  .contact-list svg { width: 15px; height: 15px; flex: none; }
  .contact-list .accent { color: var(--brand-blue); }
  .card-back .offices {
    position: absolute;
    right: 36px; bottom: 110px;
    font-size: 14px; color: var(--ink);
  }
</style>
</head>
<body>

<section class="card card-front">
  <div class="ghost-name" aria-hidden="true">NORVANE</div>
  <div class="wordmark">NORVANE</div>
  <p class="tagline">Specialise in insurance and reinsurance broking<br>and consultancy for our global clients</p>
</section>

<section class="card card-back">
  <div class="ghost-name" aria-hidden="true">NORVANE</div>
  <div class="wordmark">NORVANE</div>
  <div class="person">
    <p class="person-name">Daniel Hartley</p>
    <p class="person-role">Managing Director</p>
    <ul class="contact-list">
      <li>
        <svg viewBox="0 0 24 24" fill="var(--brand-blue)" aria-hidden="true"><path d="M6.6 10.8a15.1 15.1 0 0 0 6.6 6.6l2.2-2.2c.3-.3.7-.4 1-.2 1.1.4 2.3.6 3.6.6.6 0 1 .4 1 1V20c0 .6-.4 1-1 1A17 17 0 0 1 3 4c0-.6.4-1 1-1h3.5c.6 0 1 .4 1 1 0 1.3.2 2.5.6 3.6.1.3 0 .7-.2 1z"/></svg>
        044-987 654 321
      </li>
      <li>
        <svg viewBox="0 0 24 24" fill="var(--brand-blue)" aria-hidden="true"><path d="M2 5h20v14H2z" fill="none" stroke="var(--brand-blue)" stroke-width="2"/><path d="M2 5l10 8 10-8" fill="none" stroke="var(--brand-blue)" stroke-width="2"/></svg>
        info@norvane-broking.com
      </li>
      <li>
        <svg viewBox="0 0 24 24" fill="none" stroke="var(--brand-blue)" stroke-width="2" aria-hidden="true"><circle cx="12" cy="12" r="9.5"/><ellipse cx="12" cy="12" rx="4" ry="9.5"/><path d="M2.5 12h19M4 7h16M4 17h16"/></svg>
        <span>www.<span class="accent">norvane-broking</span>.com</span>
      </li>
    </ul>
  </div>
  <p class="offices">Malaysia and Dubai</p>
</section>

</body>
</html>
```